A new customer-driven VC fund for Enterprise IT Startups

I am bringing together a global group of customers (CIOs, CTOs, CISOs of Beacon 3000 companies) to help me identify and diligence best-of-breed Enterprise IT startups so I can invest in them via my new venture capital fund, Larkfen Ventures. In many ways, this is a new model for a VC fund and my goal is to revolutionize Venture Capital so that we hit the bull's eye in investing way more often in what is otherwise a guessing game for most VCs. So in the website, I'd like to capture the essences of global reach, best-of-breed, breakthrough innovation. I also want it to convey the ability of Larkfen Ventures to create category winners (i.e., if you want to be a market leader as a startup, you must take an investment from Larkfen Ventures).
My current website is www.larkfen-ventures.example - please use the content from the website within your design but please DO NOT use the design elements from the current website. INSTEAD, I'm looking for new and creative ideas on how I can leverage the existing content in a more appealing design -- any designs that look remotely similar to the existing website will be immediately declined.
I also want to ensure that the web design is mobile friendly.
Target Market(s)
Startup founders, potential investors, and other VCs
Industry/Entity Type
Venture Capital
Coding
Coded - Design and coding required
Number of Pages Required
1 page
Look and feel
Each slider illustrates characteristics of the customer's brand and the style your logo design should communicate.

```html
<!DOCTYPE html>
<html lang="en">
<head>
<meta charset="utf-8">
<title>Larkfen Ventures</title>
<link href="https://fonts.googleapis.com/css2?family=Roboto:wght@400;500;700&family=Montserrat:wght@400;500;600&display=swap" rel="stylesheet">
<style>
:root{
  --ink:#111111;
  --muted:#444a55;
  --brand:#0b63c8;
  --brand-deep:#0a4fb8;
  --accent:#2f74f0;
  --sky:#cfe9f8;
  --label:#1a5fb4;
  --mist:#e9eff7;
  --teal:#2bb5c8;
  --footer:#3d7bf5;
  --white:#ffffff;
}
*{box-sizing:border-box;margin:0;padding:0}
html,body{width:1200px;height:4114px;overflow:hidden;background:var(--white)}
body{position:relative;font-family:"Montserrat",sans-serif;color:var(--ink)}
.abs{position:absolute}
h1,h2,h3{font-family:"Roboto",sans-serif;font-weight:700;text-transform:uppercase;color:var(--ink)}
.section-title{position:absolute;left:0;width:1200px;text-align:center;font-size:28px;line-height:43px}
.lead{position:absolute;text-align:center;font-size:15px;line-height:20px;color:var(--muted)}

/* hero */
.logo{left:67px;top:48px;display:flex;align-items:center;gap:12px;font-family:"Montserrat",sans-serif;font-weight:600;font-size:26px;color:#1d2b4a}
.logo-mark{width:26px;height:26px;background:var(--brand)}
.hero-blob{left:540px;top:0}
.hero-art{left:700px;top:60px;width:470px;height:440px;border-radius:40px;background:linear-gradient(160deg,#3b8ae6,#0b5fd0);opacity:.55}
.hero-title{left:70px;top:205px;font-size:28px;line-height:43px;width:440px}
.hero-copy{left:70px;top:355px;width:400px;font-size:11.5px;line-height:17px;color:var(--muted)}
.btn{left:70px;top:457px;width:130px;height:40px;background:var(--brand);color:var(--white);font-size:15px;font-weight:500;display:flex;align-items:center;justify-content:center;letter-spacing:.3px}

/* who */
.who-art{left:0;top:750px;width:408px;height:417px;background:radial-gradient(circle at 60% 45%,#dfe6fb 0,#c7d3f7 55%,#eef2fd 75%);border-radius:0 200px 40px 0}
.who-title{left:572px;top:630px;font-size:27px}
.who-copy{left:578px;top:680px;width:400px;font-size:17px;line-height:25px;color:var(--muted)}
.info-card{width:198px;height:209px;background:var(--white);box-shadow:0 4px 14px rgba(0,0,0,.14);padding:20px 12px}
.info-card h3{font-family:"Montserrat",sans-serif;font-weight:500;font-size:13px;line-height:22px;color:var(--ink)}
.info-card p{font-size:8px;line-height:12px;color:#333;margin-top:8px}
.info-card svg{display:block;margin-top:8px}

/* numbers */
.stat{width:198px;height:64px;background:var(--sky);text-align:center;padding-top:10px;box-shadow:0 4px 10px rgba(0,0,0,.08)}
.stat b{display:block;font-family:"Montserrat",sans-serif;font-weight:500;font-size:15px}
.stat span{display:block;font-size:8px;line-height:11px;margin:5px 18px 0;color:#333}
.focus{width:140px;text-align:center}
.focus svg{display:block;margin:0 auto}
.focus span{display:block;font-family:"Roboto",sans-serif;font-weight:500;font-size:12.5px;line-height:20px;color:var(--label);margin-top:14px}
.mist{background:var(--mist)}

/* themes */
.theme{width:300px;text-align:center}
.theme h3{font-family:"Montserrat",sans-serif;font-weight:500;font-size:13.5px;line-height:23px}
.theme-img{width:134px;height:134px;border-radius:50%;margin:24px auto 0}

/* team */
.member{top:2614px;width:230px;height:243px;background:var(--white);box-shadow:0 4px 16px rgba(0,0,0,.12);text-align:center}
.portrait{width:140px;height:140px;border-radius:50%;border:3px solid var(--teal);background:linear-gradient(180deg,#d7dde3,#8d969f);margin:20px auto 0}
.member h3{font-family:"Montserrat",sans-serif;font-weight:500;font-size:15.5px;text-transform:none;margin-top:12px}
.member p{font-size:12px;line-height:19px;color:var(--muted);margin-top:6px;padding:0 20px}
.dots{left:572px;top:2900px;display:flex;gap:5px}
.dots i{width:7px;height:7px;border-radius:50%;background:var(--brand-deep)}
.dots i.off{background:var(--white);border:1.5px solid var(--brand-deep)}

/* engine */
.engine{top:3260px;width:231px;height:246px;background:linear-gradient(180deg,#3a78f2,#6fbaf0);box-shadow:0 8px 18px rgba(50,110,230,.3);padding:22px 14px;color:var(--white)}
.engine h3{color:var(--white);font-size:17px;font-weight:500}
.engine svg{display:block;margin-top:10px}
.engine p{font-size:11px;line-height:17.5px;margin-top:8px}

/* footer */
.footer-wave{left:0;top:3600px}
.contact-title{left:0;top:3800px;width:1200px;text-align:center;color:var(--white);font-size:27px;font-weight:500}
.contact-copy{left:0;top:3862px;width:1200px;text-align:center;color:var(--white);font-size:14px}
.subscribe{left:238px;top:3896px;width:724px;height:74px;display:flex}
.subscribe .field{flex:1;background:var(--white);display:flex;align-items:center;padding-left:48px;font-size:18px;color:#333}
.subscribe .send{width:179px;background:#e6e6e6;display:flex;align-items:center;justify-content:center;font-size:18px;color:#222}
.rule{left:109px;top:4045px;width:976px;height:1px;background:rgba(255,255,255,.8)}
.legal{top:4066px;color:var(--white);font-size:12px}
</style>
</head>
<body>

<!-- Hero -->
<svg class="abs hero-blob" width="660" height="610" viewBox="0 0 660 610" aria-hidden="true">
  <defs><linearGradient id="heroGrad" x1="0" y1="0" x2="1" y2="1"><stop offset="0" stop-color="#0a55c9"/><stop offset="1" stop-color="#1e8de0"/></linearGradient></defs>
  <path d="M30 0 H660 V600 C600 615 520 605 470 560 C420 510 460 430 400 390 C330 345 210 400 140 330 C70 260 130 190 70 140 C20 100 0 40 30 0 Z" fill="url(#heroGrad)"/>
</svg>
<svg class="abs" style="left:518px;top:204px" width="44" height="40" viewBox="0 0 44 40" aria-hidden="true"><ellipse cx="22" cy="20" rx="20" ry="14" transform="rotate(-30 22 20)" fill="#0b5fd0"/></svg>
<div class="abs hero-art" role="img" aria-label="Illustration of a presenter beside a chart easel with growth graphs, a light bulb and dollar signs"></div>

<div class="abs logo"><span class="logo-mark"></span>Larkfen Ventures</div>
<h1 class="abs hero-title">We invest in Enterprise IT startups at the product-market-fit stage</h1>
<p class="abs hero-copy">We are singularly focused on helping our portfolio companies gain a massive competitive advantage by providing them access to our exclusive network of hundreds of early-adopting CIOs, CTOs, CISOs, and Channel Partners around the world to rapidly accelerate customer traction.</p>
<div class="abs btn">VIEW MORE</div>

<!-- Who we are -->
<div class="abs who-art" role="img" aria-label="Illustration of two people working on laptops among gears and a plant"></div>
<h2 class="abs who-title">Who we are</h2>
<p class="abs who-copy">We only invest in post-product, post-revenue Enterprise IT startups. Usually, this means you're at Seed Extension to Series A stage</p>

<svg class="abs" style="left:770px;top:880px" width="200" height="300" viewBox="0 0 200 300" aria-hidden="true" fill="none" stroke="#3b6fc4" stroke-width="1.3" stroke-dasharray="4 4">
  <path d="M5 16 C80 30 150 50 165 90"/>
  <path d="M165 160 C120 190 80 230 45 290"/>
</svg>

<div class="abs info-card" style="left:577px;top:775px">
  <h3>CUSTOMERS</h3>
  <svg width="40" height="40" viewBox="0 0 40 40" fill="none" stroke="#222" stroke-width="1.4"><circle cx="20" cy="10" r="4"/><circle cx="8" cy="18" r="4"/><circle cx="32" cy="18" r="4"/><path d="M12 38v-6a8 8 0 0 1 16 0v6M0 34a8 8 0 0 1 14-4M40 34a8 8 0 0 0-14-4"/></svg>
  <p>Hundreds of the earliest-adopting CIOs, CTOs, and CISOs from Beacon 10 to Global 3000 to Cloud-First companies are a part of our exclusive network. An investment from Larkfen Ventures will give you immediate and exclusive access to hundreds of buyers around the world.</p>
</div>
<div class="abs info-card" style="left:933px;top:898px">
  <h3>OUR INVESTMENT PHILOSOPHY</h3>
  <svg width="40" height="40" viewBox="0 0 40 40" fill="none" stroke="#222" stroke-width="1.4"><circle cx="20" cy="14" r="10"/><path d="M23 10h-4a2 2 0 0 0 0 4h2a2 2 0 0 1 0 4h-4M20 8v2M20 18v2M4 36h8l6-4h10M4 30h6l4-2"/></svg>
  <p>We only invest in startups that have broad &amp; immediate applicability across a global CIO base and are solving critical problems. To give our portfolio companies a truly unfair competitive advantage, we do not invest in competitive startups</p>
</div>
<div class="abs info-card" style="left:617px;top:1091px">
  <h3>CUSTOMER-LED INVESTMENTS</h3>
  <svg width="42" height="42" viewBox="0 0 42 42" fill="none" stroke="#222" stroke-width="1.4"><circle cx="21" cy="21" r="18"/><path d="M8 12c4 2 6 0 9 4s-2 6 2 9 0 8 0 10M26 4c-2 4 2 6 6 6s4 6 6 8M30 28c-2 2-1 5 1 7"/></svg>
  <p>Expanding globally is no simple exercise. Our network of Global IT Execs will provide on-the-ground intelligence, referrals, and influence as you conquer new geographies</p>
</div>

<!-- Numbers -->
<div class="abs mist" style="left:0;top:1790px;width:190px;height:590px;border-radius:0 120px 200px 0"></div>
<h2 class="section-title" style="top:1405px">Strength in numbers &amp;<br>investment focus areas</h2>
<p class="lead" style="left:350px;top:1516px;width:500px;font-size:17px;line-height:25px">We collect and analyze monthly purchase intent data from a global network of IT decision-makers.</p>

<div class="abs stat" style="left:144px;top:1617px"><b>500+</b><span>Early adopting, influential CIOs, CTOs, CISOs and IT decision-makers</span></div>
<div class="abs stat" style="left:382px;top:1617px"><b>$100B+</b><span>Annual enterprise technology purchasing budget across our network</span></div>
<div class="abs stat" style="left:620px;top:1617px"><b>15</b><span>Countries represented in our current network</span></div>
<div class="abs stat" style="left:858px;top:1617px"><b>550+</b><span>Purchase intent data points collected monthly</span></div>

<div class="abs focus" style="left:152px;top:1726px">
  <svg width="64" height="70" viewBox="0 0 64 70" fill="none" stroke="#111" stroke-width="2.4"><path d="M32 4l26 10v18c0 18-12 28-26 34C18 60 6 50 6 32V14z"/><circle cx="32" cy="35" r="14"/><path d="M25 35l5 5 10-10"/></svg>
  <span>SECURITY</span>
</div>
<div class="abs focus" style="left:288px;top:1726px">
  <svg width="66" height="70" viewBox="0 0 66 70" fill="none" stroke="#111" stroke-width="2"><path d="M33 8c-6-6-18-2-18 6-8 2-10 12-4 16-6 6-2 16 6 16 2 8 12 10 16 4V8zM33 8v42"/><path d="M33 16h12M45 16v-6M33 28h20M33 40h12M45 40v8M53 28h6"/><circle cx="45" cy="8" r="2"/><circle cx="61" cy="28" r="2"/><circle cx="45" cy="50" r="2"/></svg>
  <span>AI &amp; ML</span>
</div>
<div class="abs focus" style="left:438px;top:1720px">
  <svg width="70" height="70" viewBox="0 0 70 70" fill="none" stroke="#111" stroke-width="2"><circle cx="35" cy="35" r="9"/><circle cx="14" cy="14" r="8"/><circle cx="56" cy="14" r="8"/><circle cx="14" cy="56" r="8"/><circle cx="56" cy="56" r="8"/><path d="M20 20l8 8M50 20l-8 8M20 50l8-8M50 50l-8-8"/></svg>
  <span>NETWORKING &amp;<br>ARCHITECTURE</span>
</div>
<div class="abs focus" style="left:617px;top:1722px">
  <svg width="70" height="66" viewBox="0 0 70 66" fill="none" stroke="#111" stroke-width="2"><path d="M18 40a12 12 0 0 1 2-24 16 16 0 0 1 30 2 11 11 0 0 1 2 22z"/><path d="M25 40v14M35 40v20M45 40v14"/><circle cx="25" cy="57" r="2.5"/><circle cx="35" cy="62" r="2.5"/><circle cx="45" cy="57" r="2.5"/></svg>
  <span>CLOUD &amp;<br>INFRASTRUCTURE</span>
</div>
<div class="abs focus" style="left:774px;top:1726px">
  <svg width="66" height="66" viewBox="0 0 66 66" fill="none" stroke="#111" stroke-width="2"><path d="M28 4h10l2 8 7 3 7-4 7 7-4 7 3 7 8 2v10l-8 2-3 7 4 7-7 7-7-4-7 3-2 8H28l-2-8-7-3-7 4-7-7 4-7-3-7-8-2V28l8-2 3-7-4-7 7-7 7 4 7-3z"/><path d="M20 33c4-8 10-8 13 0s9 8 13 0c-4-8-10-8-13 0s-9 8-13 0z"/></svg>
  <span>DEVOPS</span>
</div>
<div class="abs focus" style="left:910px;top:1726px">
  <svg width="70" height="66" viewBox="0 0 70 66" fill="none" stroke="#111" stroke-width="2"><path d="M16 46a12 12 0 0 1 2-24 16 16 0 0 1 30 2 11 11 0 0 1 4 22"/><rect x="12" y="34" width="46" height="18" rx="9"/><text x="35" y="48" text-anchor="middle" font-family="Roboto,sans-serif" font-size="13" fill="#111" stroke="none">SaaS</text></svg>
  <span>SAAS</span>
</div>

<!-- Themes -->
<h2 class="section-title" style="top:1990px">Unifying investment themes</h2>
<div class="abs theme" style="left:107px;top:2090px"><h3>NEXT-GEN ENTERPRISE<br>IT SOLUTIONS</h3><div class="theme-img" role="img" aria-label="Image of a glowing computer workstation in blue tones" style="background:radial-gradient(circle at 40% 40%,#3fa0f0,#0b3a8c 80%)"></div></div>
<div class="abs theme" style="left:420px;top:2090px"><h3>ATTACKING LARGE MARKETS<br>WITH UNIVERSAL APPLICATION</h3><div class="theme-img" role="img" aria-label="Image of colourful app tiles floating above a keyboard" style="background:radial-gradient(circle at 50% 45%,#5a7ae0,#0a2a6e 80%)"></div></div>
<div class="abs theme" style="left:769px;top:2090px"><h3>PRODUCTS AND PLATFORMS THAT<br>TAKE A HOLISTIC APPROACH</h3><div class="theme-img" role="img" aria-label="Image of layered digital platform screens in teal and purple" style="background:radial-gradient(circle at 50% 50%,#3bc0c8,#1a2b6a 80%)"></div></div>

<!-- Team -->
<h2 class="section-title" style="top:2428px">Team, investors &amp; advisors</h2>
<p class="lead" style="left:385px;top:2494px;width:430px;font-size:13.5px">We have built a world-class roster of executive advisors and mentors with exceptional go-to-market pedigrees to help our portfolio companies in their go-to-market journeys.</p>

<div class="abs member" style="left:70px"><div class="portrait" role="img" aria-label="Portrait photo of Rohan E. Marsh"></div><h3>Rohan E. Marsh</h3><p>Founder &amp; Managing Director</p></div>
<div class="abs member" style="left:347px"><div class="portrait" role="img" aria-label="Portrait photo of Daniel Krane"></div><h3>Daniel Krane</h3><p>Founder &amp; Ex CEO, Corvane</p></div>
<div class="abs member" style="left:623px"><div class="portrait" role="img" aria-label="Portrait photo of Vikram Dalal" style="margin-top:14px"></div><h3 style="margin-top:8px">Vikram Dalal</h3><p>Co-founder, Stratabyte (IPO), Lumenquery</p></div>
<div class="abs member" style="left:901px"><div class="portrait" role="img" aria-label="Portrait photo of Eitan Roval" style="margin-top:14px"></div><h3 style="margin-top:8px">Eitan Roval</h3><p>Co-founder, Fluxdata ($2B+ valuation)</p></div>
<div class="abs dots"><i></i><i></i><i class="off"></i><i></i><i></i></div>
<div class="abs mist" style="left:1068px;top:2880px;width:132px;height:170px;border-radius:90px 0 0 90px"></div>

<!-- Engine -->
<h2 class="section-title" style="top:3060px">A global GTM engine</h2>
<p class="lead" style="left:362px;top:3128px;width:476px;font-size:13.5px">We don't just make "customer intros", we partner with you each step of the way to help you navigate the complex landscape of enterprise sales, from key strategic accounts to strategic channel partners</p>

<div class="abs engine" style="left:185px"><h3>GTM Coaches</h3>
  <svg width="60" height="56" viewBox="0 0 60 56" fill="none" stroke="#fff" stroke-width="2"><path d="M4 52h52M10 52V38h10v14M25 52V30h10v22M40 52V22h10v30M8 30l14-12 10 6 18-16M42 8h8v8"/></svg>
  <p>We will partner with you to navigate the complex enterprise sales process by leveraging our executive network to provide product feedback, sales strategy, and market insights</p></div>
<div class="abs engine" style="left:473px"><h3>Strategic Partners</h3>
  <svg width="60" height="56" viewBox="0 0 60 56" fill="none" stroke="#fff" stroke-width="2"><circle cx="22" cy="16" r="8"/><circle cx="40" cy="12" r="5"/><path d="M4 46h10l10-6h14a3 3 0 0 0 0-6H26M14 46l8 6h18l16-12a3 3 0 0 0-4-4l-10 6"/></svg>
  <p>Strategic partnerships can propel a startup to the next level. Leverage our extensive network of IT Executives, Channel Partners, and OEMs to accelerate your path to becoming a category leader</p></div>
<div class="abs engine" style="left:780px"><h3>Global Ambassadors</h3>
  <svg width="60" height="60" viewBox="0 0 60 60" fill="none" stroke="#fff" stroke-width="2"><circle cx="30" cy="30" r="27"/><path d="M12 14c6 3 9 0 13 6s-3 9 3 13 0 12 0 15M38 5c-3 6 3 9 9 9s6 9 9 11M44 40c-3 3-2 8 2 11"/></svg>
  <p>Global Ambassadors<br>Expanding globally is no simple exercise. Our network of Global IT Execs will provide on-the-ground intelligence, referrals, and influence as you conquer new geographies</p></div>

<!-- Contact -->
<svg class="abs footer-wave" width="1200" height="514" viewBox="0 0 1200 514" aria-hidden="true">
  <path d="M0 110 C120 30 260 20 420 60 C560 95 650 120 780 95 C930 65 1060 5 1200 40 V514 H0 Z" fill="var(--footer)"/>
</svg>
<h2 class="abs contact-title">Get in touch</h2>
<p class="abs contact-copy">Subcribe to be the first to here about Update tips and recommendations</p>
<div class="abs subscribe"><div class="field">Enter Email</div><div class="send">Send</div></div>
<div class="abs rule"></div>
<p class="abs legal" style="left:109px">Copyright © 2022 Larkfen Ventures</p>
<p class="abs legal" style="right:115px">contact@larkfen-ventures.example</p>

</body>
</html>
```